Personal Finance Author needs a postcard

Hi there,

I am a Canadian personal finance author and have published a new book called The Wealth Compass.

I teach Millennials how to create a 6-figure portfolio through investing (https://www.dariafelt.com/)

I'm speaking at some conferences so we were going to print some postcards to hand out to attendees with our info and calls-to-action on them.

I am looking for 4x6 (horizontal) postcard (no space needed for shipping label).

Logos, Headshots and Book Cover:
https://files.cloudvaultex.com/folders/8kQpZrT2mWvN4xLbJ7sHdYc3FgA9eUoRi?usp=sharing

Both sides will be full colour. I would like a clean and simple look. Our main sites are www.DariaFelt.com and www.TheWealthCompassBook.com if you want to get a sense of style and design.
I also uploaded a few marketing materials so you can see the existing designs.

Side 1:
Get Instant Access to your Free Resources - main headline

(small bullets underneath)
- The Wealth Compass Checklist
- Financial Worksheets
- Database of Investment Tools

DariaFelt.com/Resources

At the bottom, include "Don't forget to follow Daria Felt on social media:
Linkedin: @dariafelt7
Facebook: @thewealthcompassbook Instagram: @thewealthcompassbook Twitter: @WealthCompassBk"

Side 2:
Headline - Want to work directly with Daria and The Wealth Compass team to help you make your money grow and stay safe?

Work with us to (bullet point list)...
- Hire Daria as a Keynote Speaker
- Teach Financial Literacy Workshops
- Receive Financial Coaching

Want To Learn More About How We Can Help?
DariaFelt.com/Services

Include my contact info:
Daria Felt
Author | Speaker | Investor
daria@thewealthcompassbook.com
416-555-0187

Target Market(s)

Millennials who want to learn how to save and invest their money. I focus on stock market investing, real estate investing and entrepreneurship.

Industry/Entity Type

Financial Service

Font styles to use
Sans Serif

Colors

Designer to choose colors to be used in the design.

Requirements
Must have
• Photo of Daria Felt
• The Wealth Compass logo
• Green, Gold/Yellow to match existing colours
• modern business style postcard

```html
<!DOCTYPE html>
<html lang="en">
<head>
<meta charset="utf-8">
<title>The Wealth Compass – Postcard</title>
<link rel="stylesheet" href="https://fonts.googleapis.com/css2?family=Montserrat:ital,wght@0,600;0,700;0,800;1,800;1,900&family=Oswald:wght@600&display=swap">
<style>
  :root {
    --gold: #f0c64f;
    --gold-deep: #e9b93a;
    --green: #0f5e2c;
    --ink: #111111;
    --frame: #333333;
    --white: #ffffff;
    --paper: #ffffff;
    --mist: #f3f2f0;
    --mist-dark: #e7e3df;
  }
  * { box-sizing: border-box; margin: 0; padding: 0; }
  html, body { width: 864px; height: 1200px; overflow: hidden; background: var(--paper); }
  body { position: relative; font-family: "Montserrat", Arial, sans-serif; color: var(--ink); }
  .abs { position: absolute; }

  /* ---------- Side 1 ---------- */
  .side { position: absolute; left: 32px; width: 806px; overflow: hidden; }
  .side-front { top: 28px; height: 548px; background: var(--white); }
  .front-band { left: 0; top: 0; width: 806px; height: 42px; background: var(--gold); }
  .headshot {
    left: 0; top: 42px; width: 365px; height: 506px;
    background: linear-gradient(180deg, #e2e4e6 0%, #d9dadc 40%, #6b5448 70%, #1c1c22 100%);
  }
  .book-cover {
    left: 373px; top: 70px; width: 127px; height: 182px;
    background: linear-gradient(160deg, #f4f4f2 0%, #e8e6df 55%, #2b7a45 100%);
    border-radius: 2px;
  }
  .brand { left: 520px; top: 92px; width: 260px; text-align: center; }
  .brand-name {
    font-family: "Oswald", "Arial Narrow", sans-serif; font-weight: 600;
    color: var(--green); font-size: 50px; line-height: 52px; text-transform: uppercase;
  }
  .front-panel { left: 365px; top: 263px; width: 441px; height: 285px; background: var(--gold); }
  .front-headline {
    left: 378px; top: 278px; width: 430px;
    color: var(--white); font-style: italic; font-weight: 900;
    font-size: 30px; line-height: 41px; letter-spacing: -0.5px;
  }
  .front-headline .lower { font-size: 31px; }
  .resource-list {
    left: 465px; top: 374px; list-style: none;
    font-weight: 800; font-size: 10.5px; line-height: 13.5px; text-transform: uppercase;
  }
  .url-pill {
    position: absolute; border: 2px solid var(--green); border-radius: 22px;
    color: var(--green); font-weight: 800; font-size: 17px; text-align: center;
    text-transform: uppercase; letter-spacing: 0.2px;
  }
  .url-pill svg { position: absolute; width: 18px; height: 18px; }
  .front-pill { left: 403px; top: 425px; width: 331px; height: 39px; line-height: 35px; }
  .front-pill svg { right: -10px; bottom: -12px; }
  .follow {
    left: 365px; top: 479px; width: 441px; text-align: center;
    font-weight: 700; font-size: 8.4px; color: #3a3a3a; text-transform: uppercase;
  }
  .social { font-weight: 700; font-size: 8px; color: #3a3a3a; display: flex; align-items: center; gap: 4px; }
  .social::before { content: ""; width: 7px; height: 7px; background: var(--green); border-radius: 1px; }
  .front-frame { left: 15px; top: 16px; width: 775px; height: 517px; border: 1.5px solid var(--frame); }

  /* ---------- Side 2 ---------- */
  .side-back { top: 608px; height: 548px; background: var(--white); }
  .back-band { left: 0; top: 0; width: 806px; height: 158px; background: var(--gold); }
  .back-mist { left: 0; top: 158px; width: 806px; height: 110px; background: linear-gradient(90deg, var(--white) 0%, var(--mist) 40%, var(--mist-dark) 100%); }
  .back-foot { left: 0; top: 506px; width: 806px; height: 42px; background: var(--gold); }
  .portrait {
    left: 18px; top: 135px; width: 300px; height: 413px;
    background: linear-gradient(180deg, #5a4032 0%, #c99c84 22%, #23232b 45%, #1a1a20 100%);
    border-radius: 90px 90px 0 0;
  }
  .back-headline { left: 47px; top: 32px; width: 740px; font-style: italic; font-weight: 900; text-transform: uppercase; }
  .back-headline .big { display: block; color: var(--white); font-size: 45.5px; line-height: 46px; letter-spacing: -1px; }
  .back-headline .mid { display: block; color: var(--green); font-size: 21.5px; line-height: 26px; letter-spacing: -0.3px; margin-top: 3px; }
  .back-headline .sub { display: block; color: var(--white); font-size: 20.5px; line-height: 28px; letter-spacing: -0.4px; }
  .service-list {
    left: 310px; top: 178px; list-style: none;
    color: var(--green); font-weight: 800; font-size: 18px; line-height: 23.5px; text-transform: uppercase;
  }
  .service-list li::before { content: "•"; color: var(--gold); margin-right: 6px; }
  .learn { left: 314px; top: 287px; width: 444px; text-align: center; font-weight: 800; font-size: 14.5px; text-transform: uppercase; }
  .back-pill { left: 370px; top: 314px; width: 329px; height: 39px; line-height: 35px; }
  .back-pill svg { right: -10px; bottom: -12px; }
  .contact { left: 314px; top: 378px; width: 444px; text-align: center; }
  .contact-name { color: var(--green); font-weight: 800; font-size: 27px; line-height: 32px; text-transform: uppercase; }
  .contact-role { color: var(--gold-deep); font-weight: 700; font-size: 13px; line-height: 16px; text-transform: uppercase; }
  .contact-mail { font-weight: 800; font-size: 15px; margin-top: 18px; text-transform: uppercase; }
  .contact-phone { color: var(--gold); font-weight: 800; font-size: 27px; line-height: 32px; margin-top: 5px; }
  .back-frame { left: 14px; top: 15px; width: 776px; height: 517px; border: 1.5px solid var(--frame); }
</style>
</head>
<body>

<section class="side side-front">
  <div class="abs front-band"></div>
  <div class="abs headshot" role="img" aria-label="Headshot of Daria Felt in a dark blazer against a light grey backdrop"></div>
  <div class="abs book-cover" role="img" aria-label="Stack of The Wealth Compass books"></div>
  <div class="abs brand">
    <div class="brand-name">The Wealth<br>Compass</div>
  </div>
  <div class="abs front-panel"></div>
  <h1 class="abs front-headline">GET INSTANT ACCESS<br><span class="lower">to your Free Resources</span></h1>
  <ul class="abs resource-list">
    <li>• The Wealth Compass Checklist</li>
    <li>• Financial Worksheets</li>
    <li>- Database of Investment Tools</li>
  </ul>
  <div class="url-pill front-pill">DariaFelt.com/Resources
    <svg viewBox="0 0 18 18"><path d="M2 2 L13 7 L9 8.5 L15 15 L13.5 16.5 L7.5 10 L6 14 Z" fill="#fff" stroke="#0f5e2c" stroke-width="1"/></svg>
  </div>
  <p class="abs follow">Don't forget to follow Daria Felt on social media</p>
  <div class="abs social" style="left:450px; top:497px;">@dariafelt7</div>
  <div class="abs social" style="left:575px; top:497px;">@thewealthcompassbook</div>
  <div class="abs social" style="left:450px; top:512px;">@WealthCompassBk</div>
  <div class="abs social" style="left:575px; top:512px;">@thewealthcompassbook</div>
  <div class="abs front-frame"></div>
</section>

<section class="side side-back">
  <div class="abs back-band"></div>
  <div class="abs back-mist"></div>
  <div class="abs back-foot"></div>
  <div class="abs portrait" role="img" aria-label="Daria Felt standing with hand on hip, wearing a dark blazer and white top"></div>
  <h2 class="abs back-headline">
    <span class="big">Want to work directly</span>
    <span class="mid">with Daria and The Wealth Compass team</span>
    <span class="sub">to help you make your money grow and stay safe?</span>
  </h2>
  <ul class="abs service-list">
    <li>Hire Daria as a keynote speaker</li>
    <li>Teach financial literacy workshops</li>
    <li>Receive financial coaching</li>
  </ul>
  <p class="abs learn">Want to learn more about how we can help?</p>
  <div class="url-pill back-pill">DariaFelt.com/Services
    <svg viewBox="0 0 18 18"><path d="M2 2 L13 7 L9 8.5 L15 15 L13.5 16.5 L7.5 10 L6 14 Z" fill="#0f5e2c"/></svg>
  </div>
  <div class="abs contact">
    <div class="contact-name">Daria Felt</div>
    <div class="contact-role">Author | Speaker | Investor</div>
    <div class="contact-mail">daria@thewealthcompassbook.com</div>
    <div class="contact-phone">416-555-0187</div>
  </div>
  <div class="abs back-frame"></div>
</section>

</body>
</html>
```